Need a web site design for a moving company

We need to re-design our website for our moving company based in New York. Our current web site (brightcartageusa.com) is very inconvenient for our customers to navigate and finding what they are looking for. We would like a web site which can have the customers fill up the Free Moving Quote after browsing it. So we want you to be creative with overall design and a quote form. We would love to target different locations, so we want our customers to be able to switch conveniently accordingly where they are located. We have a rateloop page with testimonials, which we wanted to be there as well (not just a text, and name. Boxes with pictures, profiles, just something creative and attractive). Attached is the logo, with two options(brightcart -blue and brightcart - orange, so the colors can be used accordingly or you can use your own colors if needed (if looks the best). If surfing the inner pages, we want our customers to be able to submit a quote request if needed.

Menu:
Home Services Moving Tips Testimonials About FAQ Blog Contact Us (doesn't have to be in order)

Inner Pages:
Services, Moving Tips, Testimonials, About, FAQ, Blog (moving quote is not necessary), Contact Us

Websites as references:
fetchporters.com
holdroomly.com
calmhaulers.com
tinytruckers.com.au
cityvanline.com
finchhaulage.co.uk
shiftforus.com

Reason: We are not in rush and really need someone who can read our brief throughout. We are looking for a new web site design. It doesn't have to an updated version of our current website as most of the submitted designs are. Also not all the content from a current website should be placed into a new one (depending on a style of a new layout or design you can partially copy paste some of the content). You can be as much creative as you can, making it clean looking, flat color with attractive user interface. If a menu is too long, we can skip some of them and place them in footer. The main things we are concerned about are quote form, option of location look up (switch between locations) and reviews (at least some part of the page should be dedicated to it). If you have any questions or if our brief is not clear, please let us know about it, Thank you

Industry/Entity Type

Moving Company

```html
<!DOCTYPE html>
<html lang="en">
<head>
<meta charset="utf-8">
<title>Brightcart Movers</title>
<link rel="stylesheet" href="https://fonts.googleapis.com/css2?family=Open+Sans:ital,wght@0,300;0,400;0,600;0,700;0,800;1,400&family=Caveat:wght@500&display=swap">
<style>
:root{
  --blue:#1f86d6;
  --blue-deep:#1667b8;
  --red:#ea4a50;
  --green:#4dba4f;
  --ink:#2b3440;
  --muted:#7c8691;
  --soft:#f3f4f6;
  --line:#e1e4e8;
  --navy:#1c2a3a;
  --navy-deep:#142130;
  --map:#3b78c6;
  --white:#ffffff;
}
*{box-sizing:border-box;margin:0;padding:0}
html,body{width:1200px;height:2504px;overflow:hidden}
body{font-family:"Open Sans",Arial,sans-serif;color:var(--ink);background:var(--white);position:relative}
.abs{position:absolute}

/* hero */
.hero{left:0;top:0;width:1200px;height:560px;background:linear-gradient(180deg,var(--blue) 0%,var(--blue-deep) 100%);overflow:hidden}
.hero-skyline{left:0;top:150px;width:1200px;height:410px;background:linear-gradient(180deg,rgba(255,255,255,0) 0%,rgba(255,255,255,.07) 60%,rgba(255,255,255,.12) 100%)}
.topbar{left:0;top:0;width:1200px;height:62px;border-bottom:1px solid rgba(255,255,255,.18)}
.brand{left:40px;top:18px;display:flex;align-items:center;gap:10px;color:var(--white);font-weight:800;font-size:17px;letter-spacing:1.5px}
.brand-dot{width:22px;height:22px;border-radius:50%;background:var(--red)}
.top-contact{top:22px;color:var(--white);font-size:13px;display:flex;align-items:center;gap:8px}
.top-contact svg{width:16px;height:16px}
.menu-btn{left:1080px;top:21px;color:var(--white);font-size:13px;font-weight:700;letter-spacing:1px;display:flex;gap:8px;align-items:center}
.hero-title{left:0;top:122px;width:1200px;text-align:center;color:var(--white);font-weight:300;font-size:48px}
.hero-title strong{font-weight:800}
.hero-sub{left:0;top:190px;width:1200px;text-align:center;color:var(--white);font-style:italic;font-size:19px;font-family:Georgia,"Times New Roman",serif}
.hero-tag{left:0;top:238px;width:1200px;text-align:center;color:var(--white);font-weight:700;font-size:17px;letter-spacing:4px}
.btn-green{background:var(--green);color:var(--white);font-weight:700;font-size:12px;letter-spacing:1.5px;text-align:center;border-radius:3px}
.hero-btn{left:540px;top:280px;width:120px;height:38px;line-height:38px}
.quote-head{left:0;top:385px;width:1200px;text-align:center;color:var(--white);font-weight:700;font-size:19px}
.quote-head span{color:var(--red)}

.quote-form{left:140px;top:430px;width:920px;height:104px;background:var(--white);box-shadow:0 6px 18px rgba(0,0,0,.15);padding:16px;display:flex;gap:12px}
.field-grid{display:grid;grid-template-columns:repeat(2,180px);grid-auto-rows:32px;gap:10px}
.field{border:1px solid var(--line);font-size:12px;color:var(--muted);padding:0 10px;line-height:30px;position:relative}
.field.select::after{content:"";position:absolute;right:10px;top:13px;border:5px solid transparent;border-top-color:var(--ink)}
.field.message{width:372px;height:74px}
.submit{width:92px;height:74px;background:var(--red);color:var(--white);font-weight:700;font-size:13px;display:flex;align-items:center;justify-content:center}

/* service strip */
.services{left:120px;top:650px;width:960px;display:grid;grid-template-columns:repeat(4,1fr)}
.service{text-align:center}
.service svg{width:52px;height:52px}
.service h3{font-size:17px;font-weight:700;margin-top:14px}
.service p{font-size:12px;color:var(--muted);margin-top:8px;line-height:1.5;padding:0 18px}
.quality{left:0;top:858px;width:1200px;text-align:center;font-family:"Caveat",cursive;color:var(--red);font-size:21px}
.services-btn{left:520px;top:894px;width:160px;height:40px;line-height:40px}

/* detail list */
.detail{left:0;top:960px;width:1200px;height:540px;background:var(--soft)}
.detail-grid{left:100px;top:1000px;width:1000px;display:grid;grid-template-columns:1fr 1fr;row-gap:46px;column-gap:80px}
.item{display:flex;gap:20px}
.item svg{width:44px;height:44px;flex:none}
.item h4{font-size:15px;font-weight:700;color:var(--ink)}
.item p{font-size:12px;color:var(--muted);line-height:1.55;margin-top:6px}
.read{display:inline-block;margin-top:10px;font-size:10px;font-weight:700;color:var(--blue);border:1px solid var(--blue);padding:4px 10px;letter-spacing:.5px}

/* coverage */
.cover-title{left:120px;top:1646px;font-size:34px;font-weight:800;letter-spacing:1px;color:var(--ink)}
.cover-title span{color:var(--red)}
.map{left:600px;top:1540px;width:470px;height:270px;background:linear-gradient(135deg,#4a86cf,var(--map));border-radius:40px 90px 60px 30px}

/* reviews */
.reviews{left:0;top:1840px;width:1200px;height:290px;background:linear-gradient(120deg,#5b5550 0%,#8a7d70 55%,#b8aa98 100%)}
.reviews-title{left:100px;top:1866px;color:var(--white);font-size:34px;font-weight:600}
.avatar{left:100px;top:1950px;width:120px;height:120px;border-radius:50%;background:linear-gradient(160deg,#d8b89a,#a9805f);border:4px solid var(--white)}
.quote{left:250px;top:1960px;width:380px;color:var(--white);font-size:14px;line-height:1.6;font-style:italic}
.reviewer{left:250px;top:2054px;color:#f5a34a;font-weight:700;font-size:15px}
.signup{left:660px;top:1880px;width:490px;height:200px;background:var(--red);padding:30px 34px;color:var(--white)}
.signup h3{font-size:24px;font-weight:600}
.signup-row{display:flex;gap:12px;margin-top:30px}
.signup-input{flex:1;height:40px;background:var(--white);color:var(--muted);font-size:12px;line-height:40px;padding-left:12px}
.signup-btn{width:120px;height:40px;border:2px solid var(--white);text-align:center;line-height:36px;font-weight:700;font-size:12px;letter-spacing:1px}

/* press */
.press{left:60px;top:2150px;width:1080px;height:80px;display:flex;justify-content:space-between;align-items:center}
.press span{font-size:20px;color:#9aa0a6;font-weight:600}

/* footer */
.footer{left:0;top:2256px;width:1200px;height:248px;background:var(--navy);color:#c4cdd6}
.footer-cols{left:100px;top:2282px;width:1000px;display:grid;grid-template-columns:1.3fr 1fr 1fr 1fr}
.footer-cols h5{color:var(--white);font-size:16px;font-weight:700;margin-bottom:10px}
.footer-cols li{list-style:none;font-size:12px;line-height:1.9}
.social{display:flex;align-items:center;gap:8px}
.social i{width:10px;height:10px;background:var(--blue);display:inline-block}
.footer-bar{left:0;top:2462px;width:1200px;height:42px;background:var(--navy-deep);color:#9aa6b2;font-size:12px;display:flex;justify-content:center;gap:60px;align-items:center}
</style>
</head>
<body>

<section class="abs hero">
  <div class="abs hero-skyline" role="img" aria-label="Faint city skyline silhouette behind the headline"></div>
  <header class="abs topbar">
    <div class="abs brand"><span class="brand-dot"></span>BRIGHTCART MOVERS</div>
    <div class="abs top-contact" style="left:650px">
      <svg viewBox="0 0 24 24" fill="none" stroke="#fff" stroke-width="2"><path d="M5 3h4l2 5-3 2a11 11 0 0 0 6 6l2-3 5 2v4a2 2 0 0 1-2 2A17 17 0 0 1 3 5a2 2 0 0 1 2-2z"/></svg>
      <span><b>Call Now :</b> 1-800-555-0148</span>
    </div>
    <div class="abs top-contact" style="left:850px">
      <svg viewBox="0 0 24 24" fill="none" stroke="#fff" stroke-width="2"><rect x="3" y="5" width="18" height="14"/><path d="M3 6l9 7 9-7"/></svg>
      <span>info@brightcartageusa.com</span>
    </div>
    <div class="abs menu-btn">MENU
      <svg width="18" height="14" viewBox="0 0 18 14" fill="#fff"><rect width="18" height="2"/><rect y="6" width="18" height="2"/><rect y="12" width="18" height="2"/></svg>
    </div>
  </header>
  <h1 class="abs hero-title">We are the professionals you can <strong>TRUST</strong></h1>
  <p class="abs hero-sub">with your home or business move</p>
  <p class="abs hero-tag">CALL. BOOK. MOVE.</p>
  <div class="abs btn-green hero-btn">READ MORE</div>
  <h2 class="abs quote-head">Get a <span>FREE</span> Quote</h2>
</section>

<form class="abs quote-form">
  <div class="field-grid">
    <div class="field">Your Name</div>
    <div class="field">Email</div>
    <div class="field">Phone No</div>
    <div class="field select">Select Options</div>
  </div>
  <div class="field message">Your Requirement Message</div>
  <div class="submit">Submit</div>
</form>

<section class="abs services">
  <div class="service">
    <svg viewBox="0 0 48 48" fill="none" stroke="#ea4a50" stroke-width="3"><path d="M6 24L24 8l18 16"/><path d="M11 20v20h26V20"/><rect x="20" y="28" width="8" height="12"/></svg>
    <h3>Residential Moving</h3>
    <p>Tell us where, when and what you're moving. We do the rest.</p>
  </div>
  <div class="service">
    <svg viewBox="0 0 48 48" fill="none" stroke="#ea4a50" stroke-width="3"><path d="M24 44s14-14 14-25a14 14 0 0 0-28 0c0 11 14 25 14 25z"/><circle cx="24" cy="19" r="5"/></svg>
    <h3>Local Moving</h3>
    <p>Get prices and user reviews, and choose a top rated mover.</p>
  </div>
  <div class="service">
    <svg viewBox="0 0 48 48" fill="none" stroke="#ea4a50" stroke-width="3"><rect x="8" y="10" width="20" height="32"/><rect x="28" y="20" width="12" height="22"/><path d="M13 16h4M19 16h4M13 23h4M19 23h4M13 30h4M19 30h4"/></svg>
    <h3>Commercial Moving</h3>
    <p>Enter your details and lock in your guaranteed price.</p>
  </div>
  <div class="service">
    <svg viewBox="0 0 48 48" fill="none" stroke="#ea4a50" stroke-width="3"><rect x="4" y="14" width="26" height="20"/><path d="M30 20h8l6 7v7H30z"/><circle cx="12" cy="37" r="4"/><circle cx="36" cy="37" r="4"/></svg>
    <h3>Interstate Moving</h3>
    <p>That's it! Have a great move.</p>
  </div>
</section>
<p class="abs quality">Best quality services ensured</p>
<div class="abs btn-green services-btn">VIEW SERVICES</div>

<section class="abs detail"></section>
<div class="abs detail-grid">
  <div class="item">
    <svg viewBox="0 0 48 48" fill="none" stroke="#1f86d6" stroke-width="3"><path d="M24 42s12-12 12-22a12 12 0 0 0-24 0c0 10 12 22 12 22z"/><circle cx="24" cy="20" r="4"/></svg>
    <div><h4>Local Moves</h4><p>Our local moving team handles your home with care, from packing the first box to setting up the last room.</p><span class="read">READ MORE</span></div>
  </div>
  <div class="item">
    <svg viewBox="0 0 48 48" fill="none" stroke="#1f86d6" stroke-width="3"><path d="M6 24L24 8l18 16"/><path d="M11 20v20h26V20"/></svg>
    <div><h4>Residential &amp; Commercial</h4><p>Whether you are moving your family or your business, our crews plan every step around your time and budget.</p><span class="read">READ MORE</span></div>
  </div>
  <div class="item">
    <svg viewBox="0 0 48 48" fill="none" stroke="#1f86d6" stroke-width="3"><path d="M14 30s8-8 8-15a8 8 0 0 0-16 0c0 7 8 15 8 15z"/><path d="M34 42s8-8 8-15a8 8 0 0 0-16 0c0 7 8 15 8 15z"/></svg>
    <div><h4>Interstate/Long Distance Moves</h4><p>Crossing state lines? We track every load and keep you informed until your boxes arrive safely.</p><span class="read">READ MORE</span></div>
  </div>
  <div class="item">
    <svg viewBox="0 0 48 48" fill="none" stroke="#1f86d6" stroke-width="3"><path d="M6 16l18-8 18 8v18l-18 8-18-8z"/><path d="M6 16l18 8 18-8M24 24v18"/></svg>
    <div><h4>Moving Supplies</h4><p>Boxes, tape, wrap and padding in every size, delivered to your door at fair and simple prices.</p><span class="read">READ MORE</span></div>
  </div>
  <div class="item">
    <svg viewBox="0 0 48 48" fill="none" stroke="#1f86d6" stroke-width="3"><path d="M4 18L24 8l20 10v24H4z"/><rect x="12" y="26" width="24" height="16"/><path d="M12 32h24M12 37h24"/></svg>
    <div><h4>Storage</h4><p>Need short or long term space? Our clean and secure units keep your things safe between homes.</p><span class="read">READ MORE</span></div>
  </div>
  <div class="item">
    <svg viewBox="0 0 48 48" fill="none" stroke="#1f86d6" stroke-width="3"><path d="M24 6l16 6v10c0 10-7 18-16 20C15 40 8 32 8 22V12z"/><path d="M17 24l5 5 9-10"/></svg>
    <div><h4>Insurance</h4><p>Every move is covered. Pick the protection plan that fits and enjoy real peace of mind on moving day.</p><span class="read">READ MORE</span></div>
  </div>
</div>

<h2 class="abs cover-title">WE'VE GOT YOU <span>COVERED</span></h2>
<div class="abs map" role="img" aria-label="Map of the United States with served states shaded blue and New York highlighted"></div>

<section class="abs reviews" role="img" aria-label="Softly blurred photo of a family moving into a new home"></section>
<h2 class="abs reviews-title">What people are saying</h2>
<div class="abs avatar" role="img" aria-label="Portrait of a happy customer"></div>
<p class="abs quote">"The crew arrived on time, packed everything with care and had our new place set up before dinner. We could not have asked for a smoother move."</p>
<p class="abs reviewer">Daniel, NY</p>
<div class="abs signup">
  <h3>Signup for our email updates</h3>
  <div class="signup-row">
    <div class="signup-input">Email Address</div>
    <div class="signup-btn">SUBSCRIBE</div>
  </div>
</div>

<div class="abs press">
  <span>The Daily Ledger</span>
  <span>Market Street Journal</span>
  <span>Next Wire</span>
  <span>Tech Pulse</span>
  <span>Capital Weekly</span>
  <span>The Evening Post</span>
</div>

<footer class="abs footer"></footer>
<div class="abs footer-cols">
  <div><h5>What we do</h5><ul><li>Local &amp; Long Distance Moves</li><li>Full Home Relocations</li><li>Office Moving Services</li><li>Storage &amp; Packing Help</li><li>Moving Supplies Store</li></ul></div>
  <div><h5>Company</h5><ul><li>About</li><li>Careers</li><li>Press</li><li>Blog</li></ul></div>
  <div><h5>Need Help?</h5><ul><li>FAQ</li><li>Contact</li></ul></div>
  <div><h5>Connect</h5><ul><li class="social"><i></i>Friendbook</li><li class="social"><i></i>Chirper</li></ul></div>
</div>
<div class="abs footer-bar">
  <span>© Brightcart Movers LLC 2015</span>
  <span>1-800-555-0148</span>
  <span>Privacy policy &nbsp;|&nbsp; Terms</span>
</div>

</body>
</html>
```